Email signature

I am looking for an innovative and classy looking email signature that I can use with gmail.

My info:

Dale Bowen
618.442.9037
j.dale.bowen@fernmail.com
www.NorthRidgeArcheryClub.com

My logo and business card files are attached.

Font:
- Serpentine-Bold-Bold for "NORTH RIDGE"
- BrowalliaUPC for "ARCHERY CLUB"

Colors (CMYK code):
- BLACK ....... 0; 0; 0; 100;
- ORANGE ... gradient from 0; 65; 97.5; 0 to 0; 39; 97.5; 0

Dale Bowen

North Ridge Archery Club

j.dale.bowen@fernmail.com

618.442.9037

```html
<!DOCTYPE html>
<html lang="en">
<head>
<meta charset="utf-8">
<title>Dale Bowen – Email Signature</title>
<link rel="stylesheet" href="https://fonts.googleapis.com/css2?family=Barlow:wght@400;500;700&display=swap">
<style>
  :root {
    --orange: #e17a2d;
    --black: #0b0b0b;
    --white: #ffffff;
    --page: #ffffff;
  }
  html, body {
    margin: 0;
    padding: 0;
    width: 1200px;
    height: 395px;
    overflow: hidden;
    background: var(--page);
  }
  .signature {
    position: relative;
    width: 1200px;
    height: 395px;
    font-family: "Barlow", sans-serif;
  }
  .signature__card {
    position: absolute;
    left: 40px;
    top: 33px;
    width: 1133px;
    height: 327px;
    box-sizing: border-box;
    background: var(--orange);
    border: 4px solid var(--black);
    border-radius: 82px;
  }
  .brand-mark {
    position: absolute;
    left: 118px;
    top: 60px;
    width: 282px;
    height: 270px;
    display: flex;
    flex-direction: column;
    align-items: center;
    justify-content: center;
    gap: 18px;
  }
  .brand-mark__dot {
    width: 86px;
    height: 86px;
    border-radius: 50%;
    background: var(--black);
  }
  .brand-mark__name {
    margin: 0;
    color: var(--white);
    font-weight: 700;
    font-size: 31px;
    line-height: 1.1;
    text-align: center;
    text-transform: uppercase;
  }
  .person__name {
    position: absolute;
    left: 490px;
    top: 68px;
    margin: 0;
    color: var(--white);
    font-weight: 700;
    font-size: 42px;
    line-height: 1;
    letter-spacing: 0.5px;
  }
  .person__company {
    position: absolute;
    left: 490px;
    top: 126px;
    margin: 0;
    color: var(--black);
    font-weight: 500;
    font-size: 41px;
    line-height: 1.1;
  }
  .contact__bar {
    position: absolute;
    left: 464px;
    top: 224px;
    width: 7px;
    height: 108px;
    background: var(--black);
  }
  .contact {
    position: absolute;
    left: 490px;
    top: 208px;
    margin: 0;
    padding: 0;
    list-style: none;
    color: var(--white);
    font-weight: 400;
    font-size: 30px;
    line-height: 44px;
  }
</style>
</head>
<body>
  <div class="signature">
    <div class="signature__card"></div>

    <div class="brand-mark">
      <span class="brand-mark__dot"></span>
      <p class="brand-mark__name">North Ridge<br>Archery Club</p>
    </div>

    <h1 class="person__name">DALE BOWEN</h1>
    <p class="person__company">North Ridge Archery Club</p>

    <div class="contact__bar"></div>
    <ul class="contact">
      <li class="contact__email">j.dale.bowen@fernmail.com</li>
      <li class="contact__phone">618.442.9037</li>
      <li class="contact__web">www.NorthRidgeArcheryClub.com</li>
    </ul>
  </div>
</body>
</html>
```